Professional and modern website for Real Estate services company

Hi there! We're looking for a responsive, highly professional and modern (in line with Latest trends) coded website for a Real Estate services company named Portales720º (find logo attached). I will try to Explain how I picture it in my head, but feel free to step out of the script and design it as you please. The structure for the website must be as Follows: - Menu: at the top of the screen, always visible (in any page and when to scrolling down). Logo at the left hand side (clicking redirects to home), then a Services, About us, Blog and Contact and on the right hand, Estimate and Log in (just placeholder, no log in required yet). - Home: (I like https://fr.velmora.example/): a landscape picture of Madrid's skyline. Very important That at a first glance (without scrolling) you can see a box to input data of your building to get an estimate (Post code, Number of homes, Number of garages, Number of stores, Swimming pool (yes / no) Concierge (yes / no)). Should there be a small space Also for a corporate presentation video (more or less like https://www.bravunecasales.example/ but With the estimate Request box INSTEAD OF the App - however, do not take this one as example Given I just wanted to illustrate the structure). Still in the Home, bellow the first glance, I'd like to have a brief introduction of the following pages (Services, About us, Blog and Contact). This can be in a Either "square" form (like https://fr.velmora.example/) or in a "scroll" form (like https://k7portales.example/). - Services: we offer 3 sets of services, each of them composed by three specific services, Namely: * Administration Treasury Accounting Savings * Consulting Legal Technical Regulatory * Mediation Repairs Meetings Delinquency For the sake of structuring, each of the nine services will Have to written description composed of 3 small paragraphs of About 15 words. I Tend to like to Accompany With each of the services related icons / vectors, but feel free to design them as you want. - About us: content not yet defined, but will be a series of bullets / sections in Which We talk about prep or differentiating points. We can include the corporate video presentation here again. - Blog: just a space Where you can see to the blog entries (in Home, probably just show 3/4). - Contact: a fancy contact form, with map, address, telephone, e-mail and opening hours. Just to give it a bit more content, maybe include a catch phrase like "We're looking forward to meeting you!" or something like that. - Estimate: this is the Most Important page in the website (in Addition to the upper part of the Home page). Basically replicate the estimate for the home box, but maybe with a bit more design or extended, Given this is a single page just for that. - Log in: opens a drop-down with user and password (just placeholder, no log in required yet). Regarding colors, we still do not Have a color scheme, so anything in line With the logo is OK. Many thanks in advance, Martin

Target Market(s)

All ages and genders

Industry/Entity Type

Real Estate

Coding

Coded - Design and coding required

Number of Pages Required

5+ page

Font styles to use
Sans Serif

Requirements
Must have
• Blank colored background

```html
<!DOCTYPE html>
<html lang="en">
<head>
<meta charset="utf-8">
<title>Portales720º – Real Estate Services</title>
<link href="https://fonts.googleapis.com/css2?family=Roboto:wght@300;400;500;700&display=swap" rel="stylesheet">
<style>
:root{
  --orange:#d6700b;
  --orange-soft:#e38a2c;
  --ink:#3a3a3a;
  --text:#6b6b6b;
  --dark:#2a2420;
  --darker:#1b1613;
  --panel:rgba(38,30,26,.86);
  --light:#f4f4f4;
  --line:#d9d9d9;
  --white:#ffffff;
}
*{box-sizing:border-box;margin:0;padding:0}
html,body{width:1200px;height:2571px;overflow:hidden}
body{font-family:'Roboto',Arial,sans-serif;color:var(--text);background:var(--white);position:relative}
.abs{position:absolute}

/* header */
.site-header{position:absolute;left:0;top:0;width:1200px;height:103px;background:var(--white)}
.brand{position:absolute;left:94px;top:32px;display:flex;align-items:center;gap:10px;font-size:30px;font-weight:700;color:var(--ink)}
.brand-mark{width:14px;height:14px;background:var(--orange)}
.main-nav{position:absolute;top:42px;left:447px;display:flex;gap:0;font-size:12px;color:var(--ink);font-weight:500}
.main-nav a{position:absolute;white-space:nowrap;text-decoration:none;color:inherit}
.main-nav a.active{color:var(--orange);border-bottom:2px solid var(--orange);padding-bottom:6px}
.btn{position:absolute;height:36px;line-height:36px;text-align:center;font-size:12px;font-weight:500;color:var(--white);border-radius:2px}
.btn-login{left:871px;top:33px;width:101px;background:var(--orange)}
.btn-estimate{left:981px;top:33px;width:125px;background:var(--darker)}

/* hero */
.hero{position:absolute;left:0;top:103px;width:1200px;height:526px;
  background:linear-gradient(180deg,#c9824f 0%,#e39a5c 22%,#b86a45 40%,#7a4a3a 62%,#4a3630 100%)}
.hero-title{position:absolute;left:91px;top:198px;font-size:42px;line-height:50px;font-weight:500;color:var(--white)}
.estimate-box{position:absolute;left:699px;top:51px;width:407px;height:398px;background:var(--panel)}
.estimate-title{position:absolute;left:17px;top:16px;font-size:26px;font-weight:500;color:var(--orange-soft)}
.field{position:absolute;width:160px;height:34px;border-bottom:1px solid rgba(255,255,255,.45);font-size:13px;color:#e9e3de;padding-top:8px}
.field .caret{position:absolute;right:4px;top:14px;width:0;height:0;border-left:4px solid transparent;border-right:4px solid transparent;border-top:5px solid #e9e3de}
.toggle{position:absolute;width:160px;font-size:13px;color:#e9e3de}
.toggle .switch{position:absolute;right:0;top:-2px;width:34px;height:16px;border-radius:8px;background:#bdbdbd}
.toggle .switch::after{content:"";position:absolute;right:0;top:-1px;width:18px;height:18px;border-radius:50%;background:var(--white)}
.submit{position:absolute;left:96px;top:338px;width:213px;height:45px;line-height:45px;background:var(--orange);color:var(--white);text-align:center;font-size:14px;font-weight:700;border-radius:2px}

/* about */
.about{position:absolute;left:0;top:629px;width:1200px;height:358px}
.section-title{position:absolute;font-size:37px;font-weight:400;color:var(--ink)}
.section-title span{color:var(--orange)}
.lead{position:absolute;font-size:13.5px;line-height:23px;color:var(--text)}
.checks{position:absolute;list-style:none;font-size:13px;color:var(--text)}
.checks li{height:32px;display:flex;align-items:center;gap:10px}
.video{position:absolute;left:701px;top:53px;width:405px;height:239px;background:linear-gradient(135deg,#3a3634,#1d1b1a 60%,#2c2826)}
.play{position:absolute;left:162px;top:82px;width:76px;height:76px;border-radius:50%;background:rgba(0,0,0,.55);border:5px solid rgba(255,255,255,.7)}

/* services */
.services{position:absolute;left:0;top:987px;width:1200px;height:466px;background:var(--light)}
.service-card{position:absolute;top:185px;width:320px;height:206px;background:var(--light);border:1px solid var(--line)}
.service-card .corner{position:absolute;left:-1px;top:-1px;width:62px;height:56px;background:var(--orange);border-bottom-right-radius:62px 56px}
.service-card h3{position:absolute;left:65px;top:18px;font-size:21px;font-weight:400;color:var(--ink)}
.service-list{position:absolute;left:65px;top:54px;width:230px;list-style:none}
.service-list li{height:46px;display:flex;align-items:center;gap:12px;font-size:17px;color:var(--orange);border-bottom:1px solid var(--line)}
.service-list li:last-child{border-bottom:none}
.ico{width:36px;height:36px;border-radius:50%;background:#555;display:flex;align-items:center;justify-content:center;flex:none}

/* features */
.features{position:absolute;left:0;top:1453px;width:1200px;height:364px;
  background:linear-gradient(180deg,#8a4f1a 0%,#a8621f 45%,#7a4615 100%)}
.feature{position:absolute;top:110px;width:260px;text-align:center;color:var(--white)}
.feature h4{font-size:13px;font-weight:700;margin-top:14px;letter-spacing:.2px}
.feature p{font-size:13px;line-height:21px;margin-top:6px;color:#f3e4d5}

/* blog */
.blog{position:absolute;left:0;top:1817px;width:1200px;height:446px}
.post-img{position:absolute;top:197px;width:233px;height:156px}
.date{position:absolute;left:0;top:0;width:42px;height:40px;background:var(--orange);color:var(--white);font-size:11px;font-weight:700;line-height:15px;padding:5px 0 0 9px}
.post-title{position:absolute;top:200px;width:240px;font-size:21px;line-height:27px;color:var(--ink)}
.post-text{position:absolute;top:285px;width:240px;font-size:13px;line-height:21px;color:var(--text)}

/* footer */
.site-footer{position:absolute;left:0;top:2263px;width:1200px;height:257px;background:linear-gradient(180deg,#2b231d,#3a2f27 60%,#2a221c)}
.footer-col{position:absolute;top:60px;color:#eee}
.footer-col h5{font-size:13.5px;font-weight:700;padding-bottom:8px;border-bottom:1px solid rgba(255,255,255,.25);width:168px}
.quick-links{list-style:none;margin-top:12px;font-size:11.5px}
.quick-links li{height:22px;display:flex;align-items:center;gap:8px}
.quick-links li::before{content:"";border-left:4px solid #ddd;border-top:3px solid transparent;border-bottom:3px solid transparent}
.contact-list{list-style:none;margin-top:14px;font-size:11.5px;line-height:17px}
.contact-list li{display:flex;gap:12px;margin-bottom:10px}
.newsletter p{font-size:10.5px;line-height:16px;margin-top:14px;width:220px}
.newsletter .input{margin-top:10px;width:215px;border-bottom:1px solid #ddd;font-size:10.5px;padding-bottom:6px}
.newsletter .subscribe{margin-top:18px;display:inline-block;background:var(--orange);color:var(--white);font-size:9.5px;padding:5px 8px}
.social{list-style:none;margin-top:12px;font-size:12px}
.social li{height:34px;display:flex;align-items:center;gap:10px}
.social .sq{width:22px;height:22px;border-radius:2px}
.copyright{position:absolute;left:0;top:2520px;width:1200px;height:51px;background:#151210;color:#8d8178;font-size:10.5px;text-align:center;line-height:51px}
</style>
</head>
<body>

<header class="site-header">
  <div class="brand"><span class="brand-mark"></span>Portales720º</div>
  <nav class="main-nav">
    <a class="active" style="left:0">HOME</a>
    <a style="left:72px">SERVICES</a>
    <a style="left:170px">ABOUT US</a>
    <a style="left:268px">BLOG</a>
    <a style="left:338px">CONTACT</a>
  </nav>
  <div class="btn btn-login">LOGIN</div>
  <div class="btn btn-estimate">FREE ESTIMATE</div>
</header>

<section class="hero" role="img" aria-label="Madrid skyline at sunset with rooftops and a domed building">
  <h1 class="hero-title">Going Above and Beyond<br>to Find Your Next Home</h1>
  <form class="estimate-box">
    <div class="estimate-title">Get an Free Estimate</div>
    <svg class="abs" style="left:310px;top:22px" width="78" height="28" viewBox="0 0 78 28"><path d="M2 26 V12 L40 2 L76 10 V26" fill="none" stroke="rgba(255,255,255,.35)" stroke-width="1.5"/></svg>
    <div class="field" style="left:21px;top:90px">Your Name</div>
    <div class="field" style="left:225px;top:90px">Your Email ID</div>
    <div class="field" style="left:21px;top:155px">Post Code</div>
    <div class="field" style="left:225px;top:155px">Number of Homes<span class="caret"></span></div>
    <div class="field" style="left:21px;top:220px">Number of Garages<span class="caret"></span></div>
    <div class="field" style="left:225px;top:220px">Number of Stores<span class="caret"></span></div>
    <div class="toggle" style="left:21px;top:287px">Swimming Pool<span class="switch"></span></div>
    <div class="toggle" style="left:225px;top:287px">Concierge<span class="switch"></span></div>
    <div class="submit">SUBMIT NOW</div>
  </form>
</section>

<section class="about">
  <h2 class="section-title" style="left:92px;top:56px">about <span>Portales720º</span></h2>
  <p class="lead" style="left:93px;top:112px;width:530px">Lorem ipsum dolor sit amet, consectetur adipisicing elit, sed do eiusmod tempor ut incididunt labore et dolore magna aliqua. Ut enim ad minim veniam, quis nostrud exercitation ullamco laboris nisi ut aliquip ex ea commodo consequat.</p>
  <ul class="checks" style="left:93px;top:193px">
    <li><svg width="12" height="10"><path d="M1 5 L4.5 8.5 L11 1.5" fill="none" stroke="#d6700b" stroke-width="2.2"/></svg>Lorem ipsum dolor sit amet</li>
    <li><svg width="12" height="10"><path d="M1 5 L4.5 8.5 L11 1.5" fill="none" stroke="#d6700b" stroke-width="2.2"/></svg>Phasellus leo augue, cursus sed</li>
    <li><svg width="12" height="10"><path d="M1 5 L4.5 8.5 L11 1.5" fill="none" stroke="#d6700b" stroke-width="2.2"/></svg>Aliquam quis felis fringilla</li>
  </ul>
  <ul class="checks" style="left:373px;top:193px">
    <li><svg width="12" height="10"><path d="M1 5 L4.5 8.5 L11 1.5" fill="none" stroke="#d6700b" stroke-width="2.2"/></svg>Lorem ipsum dolor sit amet</li>
    <li><svg width="12" height="10"><path d="M1 5 L4.5 8.5 L11 1.5" fill="none" stroke="#d6700b" stroke-width="2.2"/></svg>Phasellus leo augue, cursus sed</li>
    <li><svg width="12" height="10"><path d="M1 5 L4.5 8.5 L11 1.5" fill="none" stroke="#d6700b" stroke-width="2.2"/></svg>Aliquam quis felis fringilla</li>
  </ul>
  <div class="video" role="img" aria-label="Corporate presentation video still: hands holding a small house">
    <div class="play"><svg class="abs" style="left:24px;top:18px" width="26" height="30"><path d="M2 2 L24 15 L2 28 Z" fill="#fff"/></svg></div>
  </div>
</section>

<section class="services">
  <h2 class="section-title" style="left:92px;top:36px">our <span>services</span></h2>
  <p class="lead" style="left:93px;top:88px;width:940px">Lorem ipsum dolor sit amet, consectetur adipisicing elit, sed do eiusmod tempor ut incididunt labore et dolore magna aliqua. Ut enim ad minim veniam, quis nostrud exercitation ullamco laboris nisi ut aliquip ex ea commodo consequat.</p>

  <article class="service-card" style="left:93px">
    <div class="corner"><svg class="abs" style="left:14px;top:10px" width="24" height="24"><circle cx="12" cy="7" r="5" fill="#fff"/><path d="M2 22 Q12 9 22 22 Z" fill="#fff"/></svg></div>
    <h3>Administration</h3>
    <ul class="service-list">
      <li><span class="ico"><svg width="18" height="18"><path d="M2 16 H16 M4 14 V10 M8 14 V6 M12 14 V3" stroke="#fff" stroke-width="2.2"/></svg></span>Treasury</li>
      <li><span class="ico"><svg width="18" height="18"><circle cx="5" cy="5" r="2" fill="#fff"/><circle cx="13" cy="13" r="2" fill="#fff"/><path d="M14 3 L4 15" stroke="#fff" stroke-width="2"/></svg></span>Accounting</li>
      <li><span class="ico"><svg width="18" height="18"><ellipse cx="9" cy="10" rx="7" ry="6" fill="#fff"/><rect x="7" y="2" width="4" height="3" fill="#fff"/></svg></span>Savings</li>
    </ul>
  </article>

  <article class="service-card" style="left:440px">
    <div class="corner"><svg class="abs" style="left:18px;top:9px" width="16" height="26"><circle cx="8" cy="4" r="3" fill="#fff"/><rect x="5" y="10" width="6" height="14" fill="#fff"/></svg></div>
    <h3>Consulting</h3>
    <ul class="service-list">
      <li><span class="ico"><svg width="18" height="18"><path d="M3 15 L10 8 M8 4 L14 10 M11 2 L16 7" stroke="#fff" stroke-width="2.2"/><rect x="2" y="15" width="10" height="2" fill="#fff"/></svg></span>Legal</li>
      <li><span class="ico"><svg width="20" height="20"><circle cx="10" cy="10" r="6" fill="none" stroke="#fff" stroke-width="3" stroke-dasharray="3 2"/><circle cx="10" cy="10" r="2.5" fill="#fff"/></svg></span>Technical</li>
      <li><span class="ico"><svg width="18" height="18"><rect x="5" y="3" width="8" height="12" rx="2" fill="none" stroke="#fff" stroke-width="2"/><path d="M5 9 H13" stroke="#fff" stroke-width="2"/></svg></span>Regulatory</li>
    </ul>
  </article>

  <article class="service-card" style="left:787px">
    <div class="corner"><svg class="abs" style="left:14px;top:10px" width="24" height="24"><circle cx="12" cy="7" r="5" fill="#fff"/><path d="M2 22 Q12 9 22 22 Z" fill="#fff"/></svg></div>
    <h3>Mediation</h3>
    <ul class="service-list">
      <li><span class="ico"><svg width="18" height="18"><path d="M3 15 L10 8" stroke="#fff" stroke-width="3"/><circle cx="12" cy="6" r="4" fill="none" stroke="#fff" stroke-width="2.2"/></svg></span>Repairs</li>
      <li><span class="ico"><svg width="20" height="18"><circle cx="6" cy="5" r="2.5" fill="#fff"/><circle cx="14" cy="5" r="2.5" fill="#fff"/><rect x="3.5" y="9" width="5" height="7" fill="#fff"/><rect x="11.5" y="9" width="5" height="7" fill="#fff"/></svg></span>Meetings</li>
      <li><span class="ico"><svg width="18" height="18"><circle cx="9" cy="9" r="7" fill="none" stroke="#fff" stroke-width="1.5"/><circle cx="9" cy="9" r="4" fill="none" stroke="#fff" stroke-width="1.5"/><circle cx="9" cy="9" r="1.2" fill="#fff"/></svg></span>Delinquency</li>
    </ul>
  </article>
</section>

<section class="features" role="img" aria-label="Tree-framed historic building in warm orange tones">
  <div class="feature" style="left:79px">
    <svg width="48" height="44" viewBox="0 0 48 44"><path d="M4 22 L24 4 L44 22 M10 18 V40 H38 V18" fill="none" stroke="#fff" stroke-width="3"/><path d="M18 28 H30 M18 33 H28" stroke="#fff" stroke-width="2.5"/></svg>
    <h4>REAL ESTATE JUDGMENT</h4>
    <p>Lorem ipsum dolor sit amet, consectetur adipiscing elit. Vivamus mattis ultrices magna eget porta.</p>
  </div>
  <div class="feature" style="left:340px">
    <svg width="44" height="48" viewBox="0 0 44 48"><circle cx="22" cy="18" r="15" fill="#fff"/><path d="M12 30 L8 46 L16 42 L22 46 L28 42 L36 46 L32 30" fill="#fff"/><path d="M22 10 L24.5 16 L31 16 L26 20 L28 26 L22 22 L16 26 L18 20 L13 16 L19.5 16 Z" fill="#a8621f"/></svg>
    <h4>PREMIUM QUALITY</h4>
    <p>Lorem ipsum dolor sit amet, consectetur adipiscing elit. Vivamus mattis ultrices magna eget porta.</p>
  </div>
  <div class="feature" style="left:605px">
    <svg width="44" height="48" viewBox="0 0 44 48"><path d="M6 26 V20 A16 16 0 0 1 38 20 V26" fill="none" stroke="#fff" stroke-width="4"/><rect x="2" y="22" width="8" height="14" rx="3" fill="#fff"/><rect x="34" y="22" width="8" height="14" rx="3" fill="#fff"/><path d="M38 36 Q36 44 26 44" fill="none" stroke="#fff" stroke-width="3"/><path d="M22 30 L16 24 A4 4 0 0 1 22 19 A4 4 0 0 1 28 24 Z" fill="#fff"/></svg>
    <h4>FRIENDLY CUSTOMER SUPPORT</h4>
    <p>Lorem ipsum dolor sit amet, consectetur adipiscing elit. Vivamus mattis ultrices magna eget porta.</p>
  </div>
  <div class="feature" style="left:857px">
    <svg width="58" height="44" viewBox="0 0 58 44"><circle cx="36" cy="22" r="16" fill="none" stroke="#fff" stroke-width="3.5"/><path d="M36 12 V22 L43 27" fill="none" stroke="#fff" stroke-width="3"/><path d="M2 14 H18 M6 22 H18 M10 30 H20" stroke="#fff" stroke-width="3"/></svg>
    <h4>WE SAVE YOUR TIME</h4>
    <p>Lorem ipsum dolor sit amet, consectetur adipiscing elit. Vivamus mattis ultrices magna eget porta.</p>
  </div>
</section>

<section class="blog">
  <h2 class="section-title" style="left:92px;top:50px">recent <span>blog post</span></h2>
  <p class="lead" style="left:93px;top:106px;width:940px">Lorem ipsum dolor sit amet, consectetur adipisicing elit, sed do eiusmod tempor ut incididunt labore et dolore magna aliqua. Ut enim ad minim veniam, quis nostrud exercitation ullamco laboris nisi ut aliquip ex ea commodo consequat.</p>

  <div class="post-img" style="left:93px;background:linear-gradient(160deg,#e8d6a8,#7d6a4e 45%,#3e3a30)" role="img" aria-label="House among trees in soft morning light">
    <div class="date">10<br>DEC</div>
  </div>
  <h3 class="post-title" style="left:353px">Aliquam quis felis fringilla, pretium ante sit amet, sagittis nunc.</h3>
  <p class="post-text" style="left:353px">Nam vehicula augue ac ex tincidunt, quis tristique dolor ullamcorper. Donec gravida neque cursus</p>

  <div class="post-img" style="left:614px;background:linear-gradient(150deg,#6b5a4e,#b59b84 50%,#d8cfc6)" role="img" aria-label="Team reviewing house plans on a table">
    <div class="date">09<br>DEC</div>
  </div>
  <h3 class="post-title" style="left:873px">Cum sociis natoque penatibus et magnis dis parturient montes,</h3>
  <p class="post-text" style="left:873px">Nam vehicula augue ac ex tincidunt, quis tristique dolor ullamcorper. Donec gravida neque cursus</p>
</section>

<footer class="site-footer">
  <div class="footer-col" style="left:101px">
    <h5>QUICK LINKS</h5>
    <ul class="quick-links">
      <li>HOME</li><li>ABOUT</li><li>SERVICES</li><li>BLOG</li><li>CONTACT US</li>
    </ul>
  </div>
  <div class="footer-col" style="left:324px">
    <h5 style="width:284px">CONTACT INFORMATION</h5>
    <ul class="contact-list">
      <li><svg width="10" height="14"><path d="M5 13 L1 6 A4 4 0 1 1 9 6 Z" fill="#eee"/><circle cx="5" cy="5" r="1.5" fill="#2b231d"/></svg><span>2870 W. Calder Avenue Suite 140 Harlow,<br>TX 78320</span></li>
      <li><svg width="10" height="14"><path d="M3 1 Q0 7 3 13 L5 11 Q3 7 5 3 Z" fill="#eee"/></svg><span>866-410-3928</span></li>
      <li><svg width="12" height="14"><rect x="1" y="4" width="10" height="7" fill="#eee"/><path d="M1 4 L6 8 L11 4" fill="none" stroke="#2b231d"/></svg><span>info@portales720.example</span></li>
    </ul>
  </div>
  <div class="footer-col newsletter" style="left:660px">
    <h5 style="width:215px">NEWSLETTER SIGNUP</h5>
    <p>Please enter your email address below to receive our FREE newsletter</p>
    <div class="input">Your Email ID</div>
    <span class="subscribe">SUBSCRIBE</span>
  </div>
  <div class="footer-col" style="left:953px">
    <h5 style="width:188px">FOLLOW US</h5>
    <ul class="social">
      <li><span class="sq" style="background:#3b5a9a"></span>Circlebook</li>
      <li><span class="sq" style="background:#c99a1a"></span>Workline</li>
      <li><span class="sq" style="background:#2fa6de"></span>Chirper</li>
      <li><span class="sq" style="background:#4fa3d6"></span>Email</li>
    </ul>
  </div>
</footer>
<div class="copyright">Copyright© 2016 Portales720º. All Rights Received</div>

</body>
</html>
```